Menu for Traditional Persian Restraunt with Hookah - Name of Restaraunt is Venaro

We are a traditional Persian Restaraunt. We Provide Home Made Fresh Tradition Persian Meals Here in Sydney Australia
We also offer a Shisha Service in our back section of our Restaraunt.
The Restaurant Layout is like it is in IRAN, Very Unique nothing like it here in Australia. Day beds, persian Carpet, Timber Walls, Copper Lighting, Just to name a few. We want a menu that stands out and is very traditional in the Persian Way, but also is understandable for someone that isnt persian. Our Logo is a Sky Blue Colour ( which is a traditional well known colour in our country) Everything is Freshly made . We are open 7 days. Will Add Food Details andc Images in the next coming Days

Attached is our logo. I would want a space if possible to have an image of each food next to the decription. You can give me multiple option with or without, but some sort of images should be displayed even the footer and header of the menu.

I will be getting the menu printed as an A4 style book with leather front and back hard cover

I would like a SPEcial of the day Setion at the end of the menu with an emty page so i can put items on there.

Please give me ideas as i will be changing the items on special every few days

One of competitors is The Golden Ewer, Also if you have a quick look on google and type Tradition persian Food you will get an idea of the food and type of culture it is

Target Market(s)

All Cultures< Especially persians

Industry/Entity Type

It Service

Font styles to use
Sans Serif

Requirements
Must have
• Must have Blue colour Logo Provided
• Menu for Food
• Menu for Hookah
• Menu for Coffee
• Seperate Menu for Takeaway
Nice to have
• Traditional type theme in background like persian carpet( google search - hand made traditional carpet)
• needs to be easily read and undestandable

```html
<!DOCTYPE html>
<html lang="en">
<head>
<meta charset="utf-8">
<title>Venaro — Pish Ghaza Menu</title>
<link href="https://fonts.googleapis.com/css2?family=Open+Sans:ital,wght@0,400;0,600;0,700;1,400&display=swap" rel="stylesheet">
<style>
  :root {
    --teal: #1f98ae;
    --teal-dark: #17798b;
    --orange: #e0892a;
    --paper: #f4ece6;
    --paper-deep: #e7d8cf;
    --ink: #2d6f7c;
    --photo-warm: #c98a3e;
    --photo-dark: #6d4a2a;
    --plate: #f2b02c;
  }
  * { margin: 0; padding: 0; box-sizing: border-box; }
  html, body { width: 849px; height: 1200px; overflow: hidden; }
  body { font-family: "Open Sans", Arial, sans-serif; background: var(--paper); }

  .menu-page { position: relative; width: 849px; height: 1200px; overflow: hidden; }

  .carpet-pattern {
    position: absolute; inset: 0;
    background: radial-gradient(ellipse at 50% 55%, #f8f2ee 0%, var(--paper) 55%, var(--paper-deep) 100%);
  }

  .header-photo {
    position: absolute; left: -40px; top: 0; width: 929px; height: 285px;
    background: linear-gradient(160deg, var(--photo-dark) 0%, var(--photo-warm) 40%, #e9b46a 65%, #7a5a3a 100%);
    clip-path: ellipse(60% 100% at 50% 0%);
  }

  .section-title {
    position: absolute; left: 60px;
    display: flex; align-items: center; gap: 14px;
    color: var(--teal); font-weight: 700; font-size: 36px; letter-spacing: 0.5px;
  }
  .section-title svg { width: 34px; height: 18px; }
  .starters-title { top: 330px; }
  .special-title { top: 950px; }

  .dish-list { position: absolute; left: 60px; top: 405px; width: 730px; list-style: none; }
  .dish { display: flex; align-items: flex-start; height: 106px; }
  .dish-photo {
    flex: none; width: 100px; height: 62px; border-radius: 50%;
    background: radial-gradient(ellipse at 55% 50%, var(--photo-dark) 0%, #8b5a2b 35%, var(--plate) 62%, #ffffff 70%);
    border: 3px solid var(--orange);
    margin-right: 24px;
  }
  .dish-body { flex: 1; }
  .dish-line { display: flex; align-items: baseline; color: var(--teal); font-weight: 700; font-size: 17px; }
  .dish-leader { flex: 1; border-bottom: 2px dotted var(--teal); margin: 0 10px; transform: translateY(-4px); }
  .dish-note { margin-top: 8px; color: var(--orange); font-style: italic; font-size: 13px; line-height: 1.35; max-width: 600px; }

  .special-text {
    position: absolute; left: 60px; top: 1010px; width: 735px;
    color: var(--ink); font-size: 19.5px; line-height: 1.3;
  }

  .brand { position: absolute; left: 0; right: 0; top: 1135px; text-align: center; }
  .brand-name { color: var(--teal); font-weight: 600; font-size: 18px; letter-spacing: 1px; }
  .brand-dot { display: block; width: 14px; height: 14px; border-radius: 50%; background: var(--teal); margin: 0 auto 6px; }
</style>
</head>
<body>
<main class="menu-page">
  <div class="carpet-pattern" role="img" aria-label="Soft paisley carpet pattern in beige tones"></div>
  <div class="header-photo" role="img" aria-label="Photo of golden fried Persian appetisers garnished with herbs"></div>

  <h2 class="section-title starters-title">PISH GHAZA
    <svg viewBox="0 0 34 18" aria-hidden="true"><path d="M2 9h10M22 9h10M17 2l6 7-6 7-6-7z" stroke="#1f98ae" stroke-width="2" fill="none"/></svg>
  </h2>

  <ul class="dish-list">
    <li class="dish">
      <div class="dish-photo" role="img" aria-label="Photo of chelo kabab with saffron rice"></div>
      <div class="dish-body">
        <div class="dish-line"><span>Chelo Kabab Soltani</span><span class="dish-leader"></span><span>10.99$</span></div>
        <p class="dish-note">Gouché Borre, Sajé, Felfel, There are many variations of passages of Lorem Ipsum avail able.</p>
      </div>
    </li>
    <li class="dish">
      <div class="dish-photo" role="img" aria-label="Photo of chelo kabab with saffron rice"></div>
      <div class="dish-body">
        <div class="dish-line"><span>Chelo Kabab Soltani</span><span class="dish-leader"></span><span>10.99$</span></div>
        <p class="dish-note">Gouché Borre, Sajé, Felfel, There are many variations of passages of Lorem Ipsum avail able.</p>
      </div>
    </li>
    <li class="dish">
      <div class="dish-photo" role="img" aria-label="Photo of chelo kabab with saffron rice"></div>
      <div class="dish-body">
        <div class="dish-line"><span>Chelo Kabab Soltani</span><span class="dish-leader"></span><span>10.99$</span></div>
        <p class="dish-note">Gouché Borre, Sajé, Felfel, There are many variations of passages of Lorem Ipsum avail able.</p>
      </div>
    </li>
    <li class="dish">
      <div class="dish-photo" role="img" aria-label="Photo of chelo kabab with saffron rice"></div>
      <div class="dish-body">
        <div class="dish-line"><span>Chelo Kabab Soltani</span><span class="dish-leader"></span><span>10.99$</span></div>
        <p class="dish-note">Gouché Borre, Sajé, Felfel, There are many variations of passages of Lorem Ipsum avail able.</p>
      </div>
    </li>
    <li class="dish">
      <div class="dish-photo" role="img" aria-label="Photo of chelo kabab with saffron rice"></div>
      <div class="dish-body">
        <div class="dish-line"><span>Chelo Kabab Soltani</span><span class="dish-leader"></span><span>10.99$</span></div>
        <p class="dish-note">Gouché Borre, Sajé, Felfel, There are many variations of passages of Lorem Ipsum avail able.</p>
      </div>
    </li>
  </ul>

  <h2 class="section-title special-title">SPECIAL OFFER
    <svg viewBox="0 0 34 18" aria-hidden="true"><path d="M2 9h10M22 9h10M17 2l6 7-6 7-6-7z" stroke="#1f98ae" stroke-width="2" fill="none"/></svg>
  </h2>
  <p class="special-text">Contrary to popular belief, Lorem Ipsum is not simply random text. It has roots in a piece of classical Latin literature from 45 BC, making it over 2000 years old. Darian Holloway, a Latin professor at Westmere College in Oregon, looked up one of the more obscure Latin words.</p>

  <div class="brand">
    <span class="brand-dot"></span>
    <span class="brand-name">Venaro</span>
  </div>
</main>
</body>
</html>
```